Healthcare Recruitment Agency Brochure

We need our current Brochure updated as its old and dated. The brochure will be for our current and potential Clients and should provide all the necessary information regarding our services, but in a well presented, easy reading format which echoes our company Brand. The company supplies Healthcare establishments with trained healthcare Staff which can be in a variety of settings.
UPDATE: Following the submission of many designs we would like to amend the information/content to be included in the brochure and have uploaded additional information. We would like an 8 page booklet with the various sections spread out so as not to look to 'wordy' page 1 Front cover, 2 About Us, 3 Our Service, 4 Our promise, 5 Our Staff, 6 Our Ethos, 7 What Our Clients Say/Testimonials, 8 Contact Us/Back page. Please if using pictures (which is welcomed) steer away from the surgical/doctor type. We mainly provide care to the Elderly within Nursing and Residential Homes and Support Environments. Thanks
Updates

Target Market(s)

Healthcare clientell

Industry/Entity Type

Healthcare

Requirements
Must have
• Pictures, animation, easy reading, informative, tie in with website theme www.carewellstaffline.example
Nice to have
• open to ideas
Should not have
• very long text paragraphs

```html
<!DOCTYPE html>
<html lang="en">
<head>
<meta charset="utf-8">
<title>Carewell Staffline – Brochure</title>
<link rel="stylesheet" href="https://fonts.googleapis.com/css2?family=Montserrat:ital,wght@0,400;0,600;0,700;1,400;1,600&family=Oswald:wght@500;700&display=swap">
<style>
:root{
  --blue:#1f56a3;
  --teal:#1aa58c;
  --page:#eef6f6;
  --page-edge:#dcecec;
  --ink:#3a3f44;
  --bg:#3b3b3b;
  --photo-warm:#cdb8a2;
  --photo-green:#7d9a5a;
}
*{box-sizing:border-box;margin:0;padding:0}
html,body{width:810px;height:1200px;overflow:hidden}
body{background:var(--bg);font-family:"Montserrat",Arial,sans-serif;color:var(--ink);position:relative}
.spread{position:absolute;left:15px;width:780px;height:555px;display:flex;border-bottom:3px solid var(--teal);box-shadow:0 10px 24px rgba(0,0,0,.45)}
.spread--covers{top:25px}
.spread--inside{top:615px;border-bottom-color:var(--blue)}
.page{position:relative;width:390px;height:100%;background:linear-gradient(160deg,#f6fbfb,var(--page) 60%,var(--page-edge));overflow:hidden}
.page--left{box-shadow:inset -10px 0 14px -10px rgba(0,0,0,.25)}
.page--right{box-shadow:inset 10px 0 14px -10px rgba(0,0,0,.2)}
.photo{position:absolute;border-radius:50%;border:4px solid var(--blue)}
.photo--teal{border-color:var(--teal)}
.label{position:absolute;display:flex;font-family:"Oswald",sans-serif;font-size:15px;letter-spacing:.5px;text-transform:uppercase;line-height:1}
.label span{padding:4px 8px;color:#fff}
.label .a{background:var(--teal);font-weight:500}
.label .b{background:var(--blue);font-weight:700}
.brand{position:absolute;font-family:"Montserrat",sans-serif;font-weight:600;color:var(--blue);display:flex;align-items:center;gap:6px;white-space:nowrap}
.brand i{display:block;border-radius:50%;background:var(--teal);flex:none}
.branches{position:absolute;left:40px;top:360px;font-size:7.4px;line-height:1.45}
.branch{margin-bottom:5px}
.branch h4{color:var(--blue);font-weight:700;font-size:7.4px;text-transform:uppercase}
.row{display:flex;align-items:center;gap:4px}
.row svg{flex:none}
.contact{margin-top:6px}
.socials{position:absolute;left:285px;top:470px;display:flex;gap:8px}
.socials i{width:13px;height:13px;border-radius:50%;background:var(--teal);display:block}
.tagline{position:absolute;left:220px;top:404px;width:150px;font-size:7.4px;line-height:1.35;font-weight:600}
.tagline b{color:var(--blue)}
.url-pill{position:absolute;left:150px;top:474px;width:220px;height:22px;border-radius:11px;background:var(--blue);color:#fff;font-size:8px;letter-spacing:1.6px;display:flex;align-items:center;justify-content:center}
.heading{position:absolute;font-family:"Oswald",sans-serif;font-style:italic;font-size:19px;font-weight:500;color:#1c2b44;text-transform:uppercase;letter-spacing:.3px}
.heading b{color:var(--blue);font-weight:700}
.rule{position:absolute;height:1.5px;background:var(--teal)}
.copy{position:absolute;font-size:6.6px;line-height:1.4}
.copy p{margin-bottom:4px}
.hl{color:var(--blue);font-weight:700}
.pull{color:var(--blue);font-style:italic;font-weight:600;font-size:8px;line-height:1.3;margin:6px 0}
.ticks{list-style:none;border-left:1px solid var(--teal);padding-left:9px}
.ticks li{position:relative;margin-bottom:3px}
.ticks li::before{content:"";position:absolute;left:-13px;top:1px;width:6px;height:6px;border:1px solid var(--teal);border-radius:50%;background:var(--page)}
.ticks--plain{border-left:none}
.ethos-sub{font-weight:600;font-size:8px;letter-spacing:.3px}
.value{position:absolute;width:150px;border-left:1.5px solid var(--blue);padding-left:7px;font-size:6.6px;line-height:1.4}
.value h5{font-family:"Oswald",sans-serif;font-style:italic;font-weight:500;color:var(--blue);font-size:10px;text-transform:uppercase;margin-bottom:2px}
.swoosh{position:absolute}
</style>
</head>
<body>

<section class="spread spread--covers">
  <div class="page page--left back-cover">
    <svg class="swoosh" width="390" height="555" viewBox="0 0 390 555" aria-hidden="true"><circle cx="250" cy="250" r="160" fill="none" stroke="#d2e6e6" stroke-width="14"/><polyline points="130,345 330,300 390,300" fill="none" stroke="var(--teal)" stroke-width="3"/></svg>
    <div class="photo" role="img" aria-label="Photo of a carer walking with an elderly man in a wheelchair in a park" style="left:55px;top:100px;width:230px;height:230px;background:radial-gradient(circle at 60% 45%,#a9c6e6,var(--photo-green) 60%,#5a7636)"></div>
    <div class="label" style="left:40px;top:335px"><span class="a">Our</span><span class="b">Branches</span></div>
    <div class="branches">
      <div class="branch"><h4>Northbrook | Westshire</h4>
        <div class="row"><svg width="6" height="8" viewBox="0 0 6 8"><path d="M3 8C1 5 0 4 0 3a3 3 0 016 0c0 1-1 2-3 5z" fill="var(--teal)"/></svg>14 Orchard Row, Northbrook, Westshire, NB1 4AA</div>
        <div class="row"><svg width="7" height="7" viewBox="0 0 7 7"><path d="M1 0l2 2-1 1 2 2 1-1 2 2-1 1C3 7 0 4 0 1z" fill="var(--teal)"/></svg>01000 100 101</div></div>
      <div class="branch"><h4>Elmford | Westshire</h4>
        <div class="row"><svg width="6" height="8" viewBox="0 0 6 8"><path d="M3 8C1 5 0 4 0 3a3 3 0 016 0c0 1-1 2-3 5z" fill="var(--teal)"/></svg>80 Mill Lane, Elmford, EF2 3BB</div>
        <div class="row"><svg width="7" height="7" viewBox="0 0 7 7"><path d="M1 0l2 2-1 1 2 2 1-1 2 2-1 1C3 7 0 4 0 1z" fill="var(--teal)"/></svg>01000 200 202</div></div>
      <div class="branch"><h4>Riverside | Westshire</h4>
        <div class="row"><svg width="6" height="8" viewBox="0 0 6 8"><path d="M3 8C1 5 0 4 0 3a3 3 0 016 0c0 1-1 2-3 5z" fill="var(--teal)"/></svg>5 Linden Court, Abbey Hill, Riverside, Westshire, RV3 7CC</div>
        <div class="row"><svg width="7" height="7" viewBox="0 0 7 7"><path d="M1 0l2 2-1 1 2 2 1-1 2 2-1 1C3 7 0 4 0 1z" fill="var(--teal)"/></svg>01000 300 303</div></div>
      <div class="branch"><h4>Southvale | Westshire</h4>
        <div class="row"><svg width="6" height="8" viewBox="0 0 6 8"><path d="M3 8C1 5 0 4 0 3a3 3 0 016 0c0 1-1 2-3 5z" fill="var(--teal)"/></svg>31b High Street, Southvale, Westshire, SV4 2DD</div>
        <div class="row"><svg width="7" height="7" viewBox="0 0 7 7"><path d="M1 0l2 2-1 1 2 2 1-1 2 2-1 1C3 7 0 4 0 1z" fill="var(--teal)"/></svg>01000 400 404</div></div>
      <div class="contact">
        <div class="row"><svg width="8" height="6" viewBox="0 0 8 6"><rect x=".5" y=".5" width="7" height="5" fill="none" stroke="var(--teal)"/><path d="M.5.5L4 3 7.5.5" fill="none" stroke="var(--teal)"/></svg>info@carewellstaffline.example</div>
        <div class="row"><svg width="7" height="7" viewBox="0 0 7 7"><circle cx="3.5" cy="3.5" r="3.5" fill="var(--teal)"/></svg>www.carewellstaffline.example</div>
      </div>
    </div>
    <div class="brand" style="left:262px;top:446px;font-size:11px"><i style="width:8px;height:8px"></i>Carewell Staffline</div>
    <div class="socials"><i></i><i></i><i></i></div>
  </div>

  <div class="page page--right front-cover">
    <svg class="swoosh" width="390" height="555" viewBox="0 0 390 555" aria-hidden="true"><circle cx="0" cy="250" r="160" fill="none" stroke="#d2e6e6" stroke-width="14"/><polyline points="0,300 200,300 390,255" fill="none" stroke="var(--teal)" stroke-width="3"/></svg>
    <div class="brand" style="left:110px;top:40px;font-size:22px"><i style="width:14px;height:14px"></i>Carewell Staffline</div>
    <div class="photo" role="img" aria-label="Photo of a smiling care worker in uniform supporting an elderly woman at home" style="left:60px;top:85px;width:285px;height:285px;background:radial-gradient(circle at 55% 40%,#f1e3cf,var(--photo-warm) 60%,#9c8672)"></div>
    <div class="label" style="left:220px;top:378px"><span class="a">Superior</span><span class="b">Solutions</span></div>
    <p class="tagline">We supply <b>qualified, experienced</b> local staff, dedicated to delivering <b>excellent services.</b></p>
    <div class="url-pill">www.carewellstaffline.example</div>
  </div>
</section>

<section class="spread spread--inside">
  <div class="page page--left about">
    <h2 class="heading" style="left:40px;top:40px">About <b>Us</b></h2>
    <div class="rule" style="left:40px;top:70px;width:320px"></div>
    <div class="copy" style="left:40px;top:78px;width:320px">
      <p>With over <span class="hl">15 years</span> of experience <span class="hl">Carewell Staffline</span> specialises in reliable recruitment solutions for the healthcare sector.</p>
      <p>We are <span class="hl">industry accredited</span> so you can rest assured that we will always be working in line with current legislation and guidelines.</p>
      <p>We strive for excellence in every aspect of our service, this includes ensuring that we are always fair, honest, and supportive of our temporary staff members, which is why we are a National Living Wage Employer.</p>
      <p class="pull">We know that our Clients often have a lot on their plate, which is why we pride ourselves on being extremely accommodating:</p>
    </div>
    <ul class="copy ticks" style="left:52px;top:186px;width:160px">
      <li>We can visit you at a time to suit you, to discuss your requirements and our service.</li>
      <li>We will give you our client application pack including everything you need to know; to start booking staff we simply need a completed client account form.</li>
      <li>We have staff available to work at the drop of a hat – we understand the need for urgency and will make it our mission to help you every time.</li>
      <li>Our friendly office staff will always be at the end of the phone to deal with your requests; we never outsource to call centres.</li>
      <li>We will never leave you waiting and always be honest and realistic in telling you whether we can help.</li>
      <li>When you have booked a staff member you will always receive their compliance form, in a format that suits you.</li>
      <li>You can choose how frequently and in which format we send you your staff rotas, we will be completely flexible to your needs.</li>
      <li>We are always interested in how we could improve; we will regularly review our service and come and visit you when requested.</li>
      <li>We will regularly send you monitoring forms so you can quickly and easily pass on your feedback about the staff members we are sending you.</li>
    </ul>
    <div class="photo photo--teal" role="img" aria-label="Photo of a team of care staff joining hands" style="left:222px;top:290px;width:165px;height:165px;background:radial-gradient(circle at 50% 40%,#ffffff,#cfe3ec 60%,#a8c4d2)"></div>
    <div class="photo photo--teal" role="img" aria-label="Photo of a carer with an elderly woman outdoors" style="left:220px;top:445px;width:85px;height:85px;background:radial-gradient(circle at 50% 45%,#e6a28a,var(--photo-green) 70%)"></div>
  </div>

  <div class="page page--right staff">
    <h2 class="heading" style="left:35px;top:40px">Our <b>Staff</b></h2>
    <div class="rule" style="left:35px;top:70px;width:320px"></div>
    <p class="copy" style="left:35px;top:76px;width:320px">All our candidates go through a thorough vetting and recruitment process and only ever commence assignments after the following:</p>
    <div class="photo" role="img" aria-label="Portrait photo of a smiling care assistant in uniform" style="left:20px;top:110px;width:135px;height:135px;background:radial-gradient(circle at 50% 40%,#e9c6ad,#b08a72 65%,#7d5e4c)"></div>
    <ul class="copy ticks ticks--plain" style="left:172px;top:100px;width:195px">
      <li>A face-to-face interview and skills assessment has been undertaken</li>
      <li>Full employment history has been recorded and verified</li>
      <li>Right to work has been submitted</li>
      <li>Fitness to work has been declared</li>
      <li>Two work related references have been obtained and verified</li>
      <li>An enhanced DBS Certificate has been provided</li>
      <li>In date, sufficient training certificates have been provided and verified or in house training courses have been attended and certificates have been issued.</li>
      <li>Registration with the appropriate bodies has been verified for Registered Nurses.</li>
      <li>A shadow shift has been completed if it is a brand new staff member</li>
      <li>An ID Badge, uniform, and timesheets have been issued</li>
    </ul>
    <div class="copy" style="left:35px;top:306px;width:320px">
      <p>We understand that it is imperative for our clients to only have extremely competent, fully trained staff supporting their existing team. We are proud to cover the standards set with in the <span class="hl">Care Certificate</span> in the training modules that we deliver to our staff.</p>
      <p>All training is refreshed on an annual basis and we ensure that up to date certificates are held by all staff at all times.</p>
    </div>
    <h2 class="heading" style="left:35px;top:356px">Our <b>Ethos</b></h2>
    <p class="copy ethos-sub" style="left:35px;top:384px">Carewell Staffline Services Ltd</p>
    <div class="rule" style="left:35px;top:397px;width:320px"></div>
    <div class="value" style="left:35px;top:405px"><h5>Honesty and Integrity.</h5>We pride ourselves on being direct and straightforward in all our communication with our clients and potential candidates.</div>
    <div class="value" style="left:205px;top:425px"><h5>Dedication.</h5>Our consultants aim to fully understand the requirements of our clients and candidates in order to find mutually beneficial solutions.</div>
    <div class="value" style="left:35px;top:462px"><h5>Service Excellence.</h5>We aim to always deliver superior services to help both employers and candidates achieve their goals.</div>
    <div class="value" style="left:205px;top:484px"><h5>Leadership.</h5>Our purpose is to become leaders in the healthcare recruitment sector, raising the bar for the entire industry.</div>
  </div>
</section>

</body>
</html>
```